Business Card Design Project

Financial planning, Insurance and Real estate - Financial Services company

Contact Information for Business Card

Looking for something simple in design -
Brindlewood Capital LLC
Brindlewood Wealth Managment

```html
<!DOCTYPE html>
<html lang="en">
<head>
<meta charset="utf-8">
<title>Brindlewood Wealth Management – Business Card</title>
<link rel="stylesheet" href="https://fonts.googleapis.com/css2?family=Lato:wght@400;700&family=Roboto+Condensed:wght@700&display=swap">
<style>
  :root {
    --page-bg: #e9e7e4;
    --card-bg: #f7f8f9;
    --card-edge: #d5d8dc;
    --brand-blue: #174f8c;
    --deep-blue: #0d3f73;
    --ink: #2f3337;
    --band-dark: #3a3c3f;
    --icon-tint: #c8d6e6;
  }
  * { margin: 0; padding: 0; box-sizing: border-box; }
  html, body { width: 1200px; height: 970px; overflow: hidden; }
  body { background: var(--page-bg); position: relative; }

  .business-card {
    position: absolute;
    left: 81px; top: 173px;
    width: 1038px; height: 623px;
    background: var(--card-bg);
    border: 1px solid var(--card-edge);
    box-shadow: 0 10px 30px rgba(0,0,0,0.12);
    overflow: hidden;
  }

  .brand {
    position: absolute;
    left: 0; right: 0; top: 70px;
    display: flex; flex-direction: column; align-items: center;
  }
  .brand-mark {
    width: 150px; height: 150px;
    border-radius: 50%;
    border: 6px solid var(--brand-blue);
  }
  .brand-name {
    margin-top: 40px;
    font-family: "Roboto Condensed", "Arial Narrow", sans-serif;
    font-weight: 700;
    font-size: 22px;
    color: var(--brand-blue);
  }

  .contact-tab {
    position: absolute;
    left: 0; top: 346px;
    width: 73px; height: 190px;
    background: var(--brand-blue);
    border-radius: 0 14px 14px 0;
  }
  .contact-tab svg { position: absolute; left: 22px; width: 26px; height: 22px; fill: var(--icon-tint); }

  .contact-list {
    position: absolute;
    left: 95px; top: 358px;
    list-style: none;
    font-family: "Lato", sans-serif;
    font-size: 22px;
    color: var(--ink);
  }
  .contact-list li { height: 46.5px; line-height: 28px; white-space: nowrap; }

  .person {
    position: absolute;
    right: 92px; top: 362px;
    text-align: right;
    font-family: "Lato", sans-serif;
  }
  .person-name { font-size: 25px; color: var(--deep-blue); font-weight: 400; line-height: 32px; }
  .person-name strong { font-weight: 700; }
  .person-title { font-size: 19px; color: #222; line-height: 28px; }
  .person-address { margin-top: 34px; font-size: 21px; font-weight: 700; color: var(--deep-blue); line-height: 33px; white-space: nowrap; }

  .accent-rule {
    position: absolute;
    left: 985px; top: 368px;
    width: 5px; height: 151px;
    background: var(--brand-blue);
  }

  .footer-bands { position: absolute; left: 0; bottom: 0; width: 1038px; height: 34px; }
</style>
</head>
<body>
  <main class="business-card">
    <div class="brand">
      <div class="brand-mark"></div>
      <div class="brand-name">Brindlewood Wealth Management</div>
    </div>

    <div class="contact-tab" aria-hidden="true">
      <svg style="top:14px" viewBox="0 0 26 22"><path d="M2 8c0-4 22-4 22 0v2h-6V8H8v2H2zM6 11h14l3 9H3z"/></svg>
      <svg style="top:60px" viewBox="0 0 26 22"><path d="M7 1l4 4-2 3c1 3 4 6 7 7l3-2 4 4-3 4C11 20 4 12 4 4z"/></svg>
      <svg style="top:106px" viewBox="0 0 26 22"><path d="M7 1h12v6H7zM2 8h22v9h-5v4H7v-4H2zM9 14v5h8v-5z"/></svg>
      <svg style="top:152px" viewBox="0 0 26 22"><path d="M2 3h22v16H2zM4 5v1l9 7 9-7V5zM4 8v9h18V8l-9 7z"/></svg>
    </div>

    <ul class="contact-list">
      <li>555.302.4418</li>
      <li>555.671.0295</li>
      <li>555.483.9160</li>
      <li>mholloway@brindlewoodwealth.com</li>
    </ul>

    <div class="person">
      <div class="person-name">Maren <strong>Holloway</strong></div>
      <div class="person-title">Chief Executive Offer</div>
      <div class="person-address">4180 Larkspur Blvd, Suite 320<br>Fairhaven, NC 27999</div>
    </div>
    <div class="accent-rule"></div>

    <svg class="footer-bands" viewBox="0 0 1038 34" aria-hidden="true">
      <rect x="0" y="8" width="640" height="26" fill="var(--band-dark)"/>
      <path d="M620 34 Q640 2 680 0 H1038 V34 Z" fill="var(--brand-blue)"/>
      <path d="M612 34 Q630 6 664 2" stroke="#d9dde2" stroke-width="4" fill="none"/>
    </svg>
  </main>
</body>
</html>
```